wooden jewelry - pearl necklaces

I sell wooden jeweler (rings and pearls) on markets, and so on. I also opened my business as a carpenter. The rings and a combination of wood and metal. The wood is special wood, not very common on Europe. I paint the rings afterwards. You can see some of the pictures on the pictures I uploaded. The pearls are made of the same kind of wood and colored in all kinds of colors. They are then assembled to bracelets. The jewelry is very individual and looks really cool and all kinds of people.

Target Market(s)

Young urban alternative with a sense of individuality

Contact Information for Business Card

Front:

Text:

„Kugelwerk“ (big)
„Malte Oswitz“ (smaler)

Back
„Holzschmuck
Herstellung von individuellem Holz- und Modeschmuck

Malte Oswitz
Tel: 015239460518
Lindgarbweg 9
83127 Kirchwald

malteoswitz@postfeld.de“

Font styles to use
Sans Serif

Requirements
Nice to have
• Nice to see a camel thorn tree on the background, this is a special wood and some of the rings are made out of this wood.

```html
<!DOCTYPE html>
<html lang="de">
<head>
<meta charset="utf-8">
<title>Kugelwerk – Visitenkarte</title>
<link rel="stylesheet" href="https://fonts.googleapis.com/css2?family=Montserrat:wght@500;600;700;800&display=swap">
<style>
  :root {
    --stage: #2b2b2e;
    --card-white: #ffffff;
    --plum: #3a2c57;
    --plum-text: #3a2c57;
    --ink: #1d1d22;
    --muted: #4a4a52;
    --frame: #ffffff;
    --label-bg: rgba(255, 255, 255, 0.78);
  }
  * { box-sizing: border-box; margin: 0; padding: 0; }
  html, body { width: 1200px; height: 900px; overflow: hidden; }
  body {
    background: var(--stage);
    font-family: "Montserrat", sans-serif;
    position: relative;
  }
  .card {
    position: absolute;
    top: 296px;
    width: 540px;
    height: 308px;
    overflow: hidden;
    box-shadow: 0 14px 30px rgba(0,0,0,0.45);
  }
  /* Front */
  .card--front { left: 40px; }
  .bead-photo {
    position: absolute; inset: 0;
    background:
      radial-gradient(circle at 20% 30%, #c98a4a 0, transparent 28%),
      radial-gradient(circle at 70% 25%, #4a2436 0, transparent 30%),
      radial-gradient(circle at 85% 70%, #e3c79a 0, transparent 30%),
      radial-gradient(circle at 35% 80%, #7a3a22 0, transparent 30%),
      radial-gradient(circle at 55% 55%, #b8323c 0, transparent 18%),
      linear-gradient(135deg, #6b3a25, #3a1f2c 45%, #a06a3a 80%, #d9b98a);
  }
  .frame {
    position: absolute;
    border: 2px solid var(--frame);
  }
  .frame--outer { inset: 26px 40px; }
  .frame--inner { inset: 36px 50px; }
  .brand-label {
    position: absolute;
    left: 110px; right: 110px; top: 92px; height: 124px;
    background: var(--label-bg);
    display: flex; flex-direction: column; align-items: center; justify-content: center;
    color: var(--ink);
  }
  .brand-name { font-size: 50px; font-weight: 800; line-height: 1; letter-spacing: 0.5px; }
  .owner-name { font-size: 25px; font-weight: 600; margin-top: 8px; }

  /* Back */
  .card--back { left: 620px; background: var(--card-white); }
  .ring-photo {
    position: absolute; right: 0; top: 0; bottom: 0; width: 300px;
    background:
      radial-gradient(ellipse at 55% 62%, rgba(190,150,170,0.45) 0, rgba(220,210,215,0.3) 25%, transparent 45%),
      linear-gradient(120deg, rgba(255,255,255,0) 0, #e8e3dc 55%, #dcd6cd);
    opacity: 0.85;
  }
  .band {
    position: absolute; left: 0; right: 0; top: 0; height: 64px;
    background: var(--plum);
    color: #fff;
    text-align: right;
    padding: 12px 22px 0 0;
  }
  .tagline { font-size: 13px; font-weight: 600; }
  .band-title { font-size: 15px; font-weight: 700; margin-top: 6px; }
  .back-content { position: absolute; left: 30px; top: 88px; }
  .back-name { font-size: 27px; font-weight: 800; color: var(--plum-text); }
  .contact {
    display: flex; margin-top: 16px;
  }
  .contact-icons {
    display: flex; flex-direction: column; gap: 12px; padding-right: 14px;
    border-right: 2px solid var(--muted); padding-top: 2px;
  }
  .contact-icons svg { width: 15px; height: 15px; fill: var(--muted); }
  .contact-lines {
    padding-left: 14px; font-size: 14px; font-weight: 600; color: var(--ink); line-height: 1.55;
  }
  .contact-lines .email { font-weight: 500; }
  .contact-lines .email span { color: var(--plum); }
</style>
</head>
<body>
  <section class="card card--front">
    <div class="bead-photo" role="img" aria-label="Fotografie bunter Holzperlen"></div>
    <div class="frame frame--outer"></div>
    <div class="frame frame--inner"></div>
    <div class="brand-label">
      <div class="brand-name">Kugelwerk</div>
      <div class="owner-name">Malte Oswitz</div>
    </div>
  </section>

  <section class="card card--back">
    <div class="ring-photo" role="img" aria-label="Fotografie eines Holzrings mit Metallkern"></div>
    <header class="band">
      <p class="tagline">Herstellung von individuellem Holz- und Modeschmuck</p>
      <p class="band-title">Holzschmuck</p>
    </header>
    <div class="back-content">
      <h1 class="back-name">Malte Oswitz</h1>
      <div class="contact">
        <div class="contact-icons">
          <svg viewBox="0 0 16 16" aria-hidden="true"><path d="M4 1h8a1 1 0 0 1 1 1v12a1 1 0 0 1-1 1H4a1 1 0 0 1-1-1V2a1 1 0 0 1 1-1zm1 2v9h6V3zm3 10a.8.8 0 1 0 0 .01z"/></svg>
          <svg viewBox="0 0 16 16" aria-hidden="true"><path d="M1 3h14v10H1zm1.5 1.2L8 8.5l5.5-4.3z"/></svg>
          <svg viewBox="0 0 16 16" aria-hidden="true"><path d="M8 1a5 5 0 0 1 5 5c0 3.5-5 9-5 9S3 9.5 3 6a5 5 0 0 1 5-5zm0 3a2 2 0 1 0 0 4 2 2 0 0 0 0-4z"/></svg>
        </div>
        <div class="contact-lines">
          <p>015239460518</p>
          <p class="email">malte<span>oswitz</span>@postfeld.de</p>
          <p>Lindgarbweg 9</p>
          <p>83127 Kirchwald</p>
        </div>
      </div>
    </div>
  </section>
</body>
</html>
```